Professional looking website for solo practitioner law practice

I have recently started up my new law practice. Currently there is just myself practicing here. I would like to have a website that provides my contact information, a map, and the different areas of law that I practice in, being Family Litigation, Wills & Estates, Corporate/Commerical, and Real Estate. I recently had a logo designed so I would like the colours of my website to be congruent with that and include the logo.
I am located in Edmonton, Alberta.

Reason: I will be away for the next few days.

Target Market(s)

individuals and families with an income of $50K+, mostly those looking for family lawyer re divorce, child support, custody and parenting, spousal support.

Industry/Entity Type

Lawyer

Number of Pages Required

4 page

Font styles to use
Serif

Colors
0355a3

Requirements
Must have
• Contact information, ability to email me, background picture(s) that are professional and fit with the legal services theme/service provided but are not single individual lawyers, gavels, or court houses. Need to have click to change the text to include information on Family Litigation, Wills & Estates, Corporate/Commercial, and Real Estate
Nice to have
• contact box
Should not have
• blog, sans serif text, testimonials, news

```html
<!DOCTYPE html>
<html lang="en">
<head>
<meta charset="utf-8">
<title>Elena Marsh Law Office</title>
<link rel="stylesheet" href="https://fonts.googleapis.com/css2?family=Cinzel:wght@400;600;700&family=Raleway:wght@400;500;600;700&display=swap">
<style>
:root{
  --brand:#0355a3;
  --brand-deep:#0a4a94;
  --brand-light:#1a6fd0;
  --ink:#2b2b2b;
  --muted:#555;
  --paper:#ffffff;
  --mist:#ebebeb;
  --card:#f3f3f3;
  --charcoal:#3a3a3a;
  --map-land:#d9dfe4;
}
*{box-sizing:border-box;margin:0;padding:0}
html,body{width:1200px;height:2446px;overflow:hidden}
body{position:relative;background:var(--paper);font-family:'Raleway',sans-serif;color:var(--ink)}
.abs{position:absolute}

/* header */
.site-header{left:0;top:0;width:1200px;height:108px;background:var(--paper)}
.brand-mark{left:98px;top:28px;width:54px;height:54px;border:3px solid var(--brand-deep)}
.brand-name{left:166px;top:30px;font-family:'Cinzel',serif;font-weight:600;color:var(--brand-deep);font-size:30px;line-height:30px}
.brand-sub{left:166px;top:62px;font-family:'Cinzel',serif;font-weight:600;color:var(--brand-deep);font-size:13px;letter-spacing:5px}
.nav-item{top:0;height:108px;line-height:130px;font-size:16px;color:#333}
.nav-item.active{background:var(--brand);color:#fff;text-align:center}
.nav-home-icon{left:32px;top:22px;width:22px;height:22px;border:2px solid #fff}

/* hero */
.hero{left:0;top:108px;width:1200px;height:504px;background:linear-gradient(180deg,#8aa3ad 0%,#5f7a86 45%,#2f3d44 100%)}
.hero-title{left:380px;top:315px;width:442px;height:83px;background:var(--brand);color:#fff;text-align:center;font-family:'Cinzel',serif;font-size:44px;line-height:83px}
.hero-band{left:0;top:545px;width:1200px;height:67px;background:rgba(10,10,10,.85);color:#fff;text-align:center;font-family:'Cinzel',serif;font-weight:600;font-size:27px;line-height:67px;letter-spacing:1px}

/* section headings */
.heading-mark{width:32px;height:32px;border:2px solid var(--brand-deep)}
.section-title{font-family:'Cinzel',serif;font-weight:600;font-size:32px;color:var(--brand-deep)}
.underline{height:2px;background:var(--brand-deep)}

/* welcome */
.welcome-text{left:98px;width:540px;font-size:12.5px;line-height:21.5px;color:#333}
.btn{background:var(--brand);color:#fff;font-size:14px;text-align:center;border-radius:6px}
.video-frame{left:695px;top:670px;width:407px;height:260px;border:4px solid #ddd;background:linear-gradient(135deg,#b9a58a,#6d7d92 55%,#3a4656);box-shadow:0 10px 20px rgba(0,0,0,.25)}
.video-bar{left:0;bottom:0;width:100%;height:30px;background:rgba(0,0,0,.55)}

/* practice */
.practice{left:0;top:985px;width:1200px;height:508px;background:linear-gradient(180deg,#0f5cb8,#0355a3 60%,#02499a)}
.practice-card{top:1170px;width:233px;height:270px;background:var(--card);border:1px solid #fff;text-align:center}
.card-title{position:absolute;left:0;top:62px;width:100%;font-size:15px;font-weight:700;color:var(--brand)}
.card-text{position:absolute;left:18px;top:92px;width:197px;font-size:12px;line-height:20px;color:#444}
.card-btn{position:absolute;left:0;bottom:0;width:100%;height:50px;line-height:48px;background:linear-gradient(180deg,#0a5cbf,var(--brand));color:#fff;font-size:15px;font-weight:600;border-top:3px solid #0a3f80}
.card-btn.dark{background:linear-gradient(180deg,#555,var(--charcoal));border-top-color:#222}
.card-icon{top:1112px;width:100px;height:100px;border-radius:50%;background:var(--brand);border:4px solid #fff}
.card-icon.dark{background:var(--charcoal)}

/* profile */
.profile{left:0;top:1493px;width:1200px;height:309px;background:var(--mist)}
.profile-text{left:348px;width:754px;font-size:12.5px;line-height:22.5px;color:#333}

/* clients */
.client-box{top:1932px;width:225px;height:88px;border:1px solid #cfcfcf;text-align:center;line-height:86px;font-size:24px;font-weight:500;color:#666}

/* footer */
.site-footer{left:0;top:2070px;width:1200px;height:305px;background:linear-gradient(90deg,#161616,#2a2a2a 50%,#141414)}
.foot-h{font-size:19px;font-weight:600;color:#fff}
.foot-list{font-size:12.5px;color:#fff;line-height:25.5px;list-style:none}
.foot-text{font-size:13.5px;color:#fff;line-height:21px}
.field{border:1px solid #bbb;border-radius:4px;color:#fff;font-size:11px;padding:10px 12px}
.office-map{left:375px;top:2282px;width:150px;height:70px;border:1px solid #888;background:linear-gradient(135deg,var(--map-land),#b9c6d1)}
.bottom-bar{left:0;top:2375px;width:1200px;height:71px;background:var(--brand);color:#fff;font-size:14px}
.social{top:2391px;width:36px;height:36px;border:2px solid #fff;border-radius:50%;display:flex;align-items:center;justify-content:center}
</style>
</head>
<body>

<header class="abs site-header">
  <div class="abs brand-mark"></div>
  <div class="abs brand-name">Elena Marsh</div>
  <div class="abs brand-sub">Law Office</div>
  <nav>
    <div class="abs nav-item active" style="left:640px;width:87px">Home<div class="abs nav-home-icon"></div></div>
    <div class="abs nav-item" style="left:752px">About Us</div>
    <div class="abs nav-item" style="left:868px">Practice Areas</div>
    <div class="abs nav-item" style="left:1018px">Contact Us</div>
  </nav>
</header>

<section class="abs hero" role="img" aria-label="Three business people in suits holding black umbrellas and orange folders in the rain"></section>
<svg class="abs" style="left:22px;top:338px" width="30" height="44" viewBox="0 0 30 44"><polyline points="24,4 6,22 24,40" fill="none" stroke="#fff" stroke-width="2"/></svg>
<svg class="abs" style="left:1148px;top:338px" width="30" height="44" viewBox="0 0 30 44"><polyline points="6,4 24,22 6,40" fill="none" stroke="#fff" stroke-width="2"/></svg>
<div class="abs hero-title">Elena Marsh</div>
<div class="abs hero-band">SOLO PRACTITIONER IN MY FIRM</div>

<section>
  <div class="abs heading-mark" style="left:98px;top:668px"></div>
  <h2 class="abs section-title" style="left:148px;top:664px">Welcome To My Law Firm</h2>
  <p class="abs welcome-text" style="top:729px">Nemo enim ipsam voluptatem quia voluptas sit aspernatur aut odit aut fugit, sed quia con sequuntur magni dolores eos qui ratione voluptatem sequi nesciunt. Neque porro quis quam est, qui dolorem ipsum quia dolor sit amet, consectetur, adipisci velit, sed quia non numquam</p>
  <p class="abs welcome-text" style="top:824px">Sed ut perspiciatis unde omnis iste natus error sit voluptatem accusantium doloremque laudantium, totam rem aperiam, eaque ipsa quae ab illo inventore.</p>
  <div class="abs btn" style="left:98px;top:888px;width:110px;height:40px;line-height:40px">Read More</div>
  <div class="abs video-frame" role="img" aria-label="Video still of two lawyers at a desk in front of bookshelves">
    <svg class="abs" style="left:177px;top:110px" width="46" height="32" viewBox="0 0 46 32"><rect width="46" height="32" rx="4" fill="rgba(0,0,0,.6)"/><polygon points="18,9 30,16 18,23" fill="#fff"/></svg>
    <div class="abs video-bar"><div class="abs" style="left:14px;top:13px;width:280px;height:4px;background:#888"><div style="width:120px;height:4px;background:var(--brand-light)"></div></div></div>
  </div>
</section>

<section class="abs practice"></section>
<div class="abs heading-mark" style="left:398px;top:1026px;border-color:#fff"></div>
<h2 class="abs section-title" style="left:450px;top:1021px;color:#fff">Areas of law Practice</h2>
<div class="abs underline" style="left:553px;top:1078px;width:218px;background:#fff"></div>

<div class="abs practice-card" style="left:98px"><div class="card-title">FAMILY LITIGATION</div><p class="card-text">We also represent small to medium sized companies that have suffered significant economic harm by the wrongful conduct of others.</p><div class="card-btn">READ MORE</div></div>
<div class="abs practice-card" style="left:355px"><div class="card-title">WILLS &amp; ESTATES</div><p class="card-text">We also represent small to medium sized companies that have suffered significant economic harm by the wrongful conduct of others.</p><div class="card-btn">READ MORE</div></div>
<div class="abs practice-card" style="left:612px"><div class="card-title">CORPORATE/COMMERICAL</div><p class="card-text">We also represent small to medium sized companies that have suffered significant economic harm by the wrongful conduct of others.</p><div class="card-btn dark">READ MORE</div></div>
<div class="abs practice-card" style="left:869px"><div class="card-title">REAL ESTATE</div><p class="card-text">We also represent small to medium sized companies that have suffered significant economic harm by the wrongful conduct of others.</p><div class="card-btn">READ MORE</div></div>

<div class="abs card-icon" style="left:164px">
  <svg width="92" height="92" viewBox="0 0 92 92"><g fill="#fff"><circle cx="46" cy="36" r="8"/><path d="M32 60c0-10 6-15 14-15s14 5 14 15z"/><circle cx="32" cy="40" r="6"/><circle cx="60" cy="40" r="6"/><path d="M21 60c0-8 4-12 10-12 2 0 3 0 4 1-3 3-4 7-4 11z"/><path d="M71 60c0-8-4-12-10-12-2 0-3 0-4 1 3 3 4 7 4 11z"/></g></svg>
</div>
<div class="abs card-icon" style="left:421px">
  <svg width="92" height="92" viewBox="0 0 92 92"><g fill="none" stroke="#fff" stroke-width="2.5"><path d="M32 24h20l10 10v34H32z"/><path d="M52 24v10h10"/><line x1="38" y1="44" x2="56" y2="44"/><line x1="38" y1="52" x2="56" y2="52"/><line x1="38" y1="60" x2="50" y2="60"/></g></svg>
</div>
<div class="abs card-icon dark" style="left:678px">
  <svg width="92" height="92" viewBox="0 0 92 92"><g fill="none" stroke="#fff" stroke-width="2.5"><line x1="46" y1="24" x2="46" y2="64"/><line x1="28" y1="32" x2="64" y2="32"/><path d="M22 48l6-16 6 16z"/><path d="M58 48l6-16 6 16z"/><line x1="36" y1="66" x2="56" y2="66"/></g></svg>
</div>
<div class="abs card-icon" style="left:935px">
  <svg width="92" height="92" viewBox="0 0 92 92"><g fill="#fff"><path d="M22 46l22-20 22 20h-6v18H28V46z"/></g><circle cx="58" cy="56" r="12" fill="#fff" stroke="var(--brand)" stroke-width="2"/><path d="M61 51c-1-1-5-2-6 0s5 3 6 5-5 3-7 1M58 48v16" fill="none" stroke="var(--brand)" stroke-width="2"/></svg>
</div>

<section class="abs profile"></section>
<svg class="abs" style="left:98px;top:1538px" width="194" height="220" viewBox="0 0 194 220" role="img" aria-label="Portrait photo of the lawyer">
  <defs><linearGradient id="portraitTone" x1="0" y1="0" x2="0" y2="1"><stop offset="0" stop-color="#e3e3e3"/><stop offset="1" stop-color="#6c6c6c"/></linearGradient></defs>
  <polygon points="97,3 191,56 191,164 97,217 3,164 3,56" fill="url(#portraitTone)" stroke="var(--brand)" stroke-width="4"/>
</svg>
<div class="abs heading-mark" style="left:348px;top:1545px"></div>
<h2 class="abs section-title" style="left:396px;top:1540px">Elena Marsh</h2>
<div class="abs underline" style="left:396px;top:1586px;width:218px"></div>
<p class="abs profile-text" style="top:1621px">Nemo enim ipsam voluptatem quia voluptas sit aspernatur aut odit aut fugit, sed quia consequuntur magni dolores eos qui ratione voluptatem sequi nesciunt. Neque porro quisquam est, qui dolorem ipsum quia dolor sit amet, con sectetur, adipisci velit, sed quia non numquam.</p>
<p class="abs profile-text" style="top:1703px">Sed ut perspiciatis unde omnis iste natus error sit voluptatem accusantium doloremque laudantium, totam rem aperiam, eaque ipsa quae ab illo inventore veritatis et quasi architecto beatae vitae dicta sunt explicabo.</p>

<section>
  <div class="abs heading-mark" style="left:474px;top:1848px"></div>
  <h2 class="abs section-title" style="left:518px;top:1843px">Our Clients</h2>
  <div class="abs underline" style="left:553px;top:1889px;width:140px"></div>
  <div class="abs client-box" style="left:98px">Northpine</div>
  <div class="abs client-box" style="left:355px">Carrow Studio</div>
  <div class="abs client-box" style="left:612px">Bellmont</div>
  <div class="abs client-box" style="left:869px">Ravelle</div>
</section>

<footer class="abs site-footer" role="img" aria-label="Dim background photo of a lawyer working at a desk"></footer>
<div class="abs" style="left:174px;top:2160px;width:60px;height:60px;border:3px solid #fff"></div>
<div class="abs" style="left:98px;top:2226px;width:212px;text-align:center;font-family:'Cinzel',serif;font-weight:600;color:#fff;font-size:27px">Elena Marsh</div>
<div class="abs" style="left:98px;top:2260px;width:212px;text-align:center;font-family:'Cinzel',serif;font-weight:600;color:#fff;font-size:13px;letter-spacing:5px">Law Office</div>

<div class="abs foot-h" style="left:375px;top:2126px">QUICK LINK</div>
<ul class="abs foot-list" style="left:375px;top:2168px">
  <li>&gt;&nbsp; Home</li><li>&gt;&nbsp; About Us</li><li>&gt;&nbsp; Practice Areas</li><li>&gt;&nbsp; Contact Us</li>
</ul>
<div class="abs office-map" role="img" aria-label="Map showing the office location in Edmonton, Alberta">
  <svg class="abs" style="left:68px;top:22px" width="14" height="20" viewBox="0 0 14 20"><path d="M7 1a6 6 0 0 0-6 6c0 4 6 12 6 12s6-8 6-12a6 6 0 0 0-6-6z" fill="var(--brand)"/><circle cx="7" cy="7" r="2.2" fill="#fff"/></svg>
</div>

<div class="abs foot-h" style="left:552px;top:2126px">CONTACT US</div>
<svg class="abs" style="left:553px;top:2170px" width="14" height="18" viewBox="0 0 14 18"><path d="M7 1a6 6 0 0 0-6 6c0 4 6 10 6 10s6-6 6-10a6 6 0 0 0-6-6z" fill="none" stroke="#fff" stroke-width="2"/><circle cx="7" cy="7" r="2" fill="#fff"/></svg>
<div class="abs foot-text" style="left:580px;top:2166px">Elena Marsh,<br>4th Floor, 118 Harlow Avenue,<br>Calder.</div>
<svg class="abs" style="left:553px;top:2246px" width="16" height="16" viewBox="0 0 16 16"><path d="M3 1l3 3-2 2c1 2 3 4 6 6l2-2 3 3-2 2C7 15 1 9 1 3z" fill="#fff"/></svg>
<div class="abs foot-text" style="left:580px;top:2244px">Help:&nbsp; + 1800 4710 2290</div>
<svg class="abs" style="left:554px;top:2290px" width="15" height="11" viewBox="0 0 15 11"><rect width="15" height="11" fill="#fff"/><polyline points="0,0 7.5,6 15,0" fill="none" stroke="#222" stroke-width="1.5"/></svg>
<div class="abs foot-text" style="left:580px;top:2284px">Mail:&nbsp; office@elenamarshlaw.example</div>

<div class="abs foot-h" style="left:831px;top:2126px">CONTACT FORM</div>
<div class="abs field" style="left:833px;top:2170px;width:130px;height:36px">Name</div>
<div class="abs field" style="left:970px;top:2170px;width:131px;height:36px">Phone</div>
<div class="abs field" style="left:833px;top:2214px;width:268px;height:66px">Message</div>
<div class="abs btn" style="left:833px;top:2296px;width:120px;height:36px;line-height:36px;font-size:12px;border-radius:3px">SEND MESSAGE</div>

<div class="abs bottom-bar"><div class="abs" style="left:98px;top:26px">© 2016 Elena Marsh.All Rights Reserved.</div></div>
<div class="abs social" style="left:950px"><svg width="16" height="12" viewBox="0 0 16 12"><rect x="1" y="1" width="14" height="10" fill="none" stroke="#fff" stroke-width="1.5"/><polyline points="1,1 8,7 15,1" fill="none" stroke="#fff" stroke-width="1.5"/></svg></div>
<div class="abs social" style="left:991px"><svg width="14" height="14" viewBox="0 0 16 16"><path d="M3 1l3 3-2 2c1 2 3 4 6 6l2-2 3 3-2 2C7 15 1 9 1 3z" fill="#fff"/></svg></div>
<div class="abs social" style="left:1032px"><svg width="12" height="16" viewBox="0 0 14 18"><path d="M7 1a6 6 0 0 0-6 6c0 4 6 10 6 10s6-6 6-10a6 6 0 0 0-6-6z" fill="none" stroke="#fff" stroke-width="2"/><circle cx="7" cy="7" r="2" fill="#fff"/></svg></div>
<div class="abs social" style="left:1072px"><svg width="16" height="16" viewBox="0 0 16 16"><circle cx="4" cy="8" r="2.2" fill="#fff"/><circle cx="12" cy="3.5" r="2.2" fill="#fff"/><circle cx="12" cy="12.5" r="2.2" fill="#fff"/><path d="M4 8l8-4.5M4 8l8 4.5" stroke="#fff" stroke-width="1.4"/></svg></div>

</body>
</html>
```